Home Page Design (+50 More Pages To Winning Designer!)

We have a 50+ page website, but we're starting with the home page. The winning designer will get all 50+ pages to design as a 2nd project, so make sure you do your best!

Quorvel is in the private jet industry and needs a re-designed website.

We have created the structure for the website and content inside of Sketvo.io (THESE ARE ONLY ROUGH A.I. GENERATED WIREFRAMES AND DO NOT NEED TO BE FOLLOWED EXACTLY) - https://www.sketvo.io/app/project/P482915_kRmQzWvLpA-TTdoNeHfx83QZaplR77wqcyhtkLm5Hu2

Take the content from the 'Home Page' under the 'Wireframe' tab on the Sketvo.io link above, but feel free to re-design the page in a better way as these are only A.I. generated wireframes.

We want a DARK theme.... High quality, luxurious feel, greyscale colors. Attached is a brand guideline (BUT THIS IS NOT A 100% BRAND GUIDELINE, YOU CAN CHANGE COLORS AND FONTS AND MAKE CHANGES IF YOU HAVE BETTER IDEAS) and attached is our logo. We are also attaching some examples of other apps and websites to give you a guideline of what we're looking for for this design project.

The final design MUST communicate luxury using high-quality imagery of large cabin luxurious private jets.

ENTRIES THAT DO NOT FOLLOW THE PROJECT BRIEF WILL BE AUTOMATICALLY DISCARDED. FOLLOW THE INSTRUCTIONS!

Industry/Entity Type

Travel

Number of Pages Required

1 page

Font styles to use
Sans Serif

Colors

Designer to choose colors to be used in the design.

Requirements
Must have
• Follow wireframe and use content in wireframe (see Sketvo.io link)

```html
<!DOCTYPE html>
<html lang="en">
<head>
<meta charset="utf-8">
<title>Quorvel — Private Jet Travel</title>
<link href="https://fonts.googleapis.com/css2?family=Saira:wght@300;400;500;600&display=swap" rel="stylesheet">
<style>
:root{
  --bg:#0b0b0b;
  --bg-alt:#121212;
  --panel:#1c1c1c;
  --line:#3a3a3a;
  --text:#f2f2f2;
  --muted:#8d8d8d;
  --dim:#5f5f5f;
  --white:#ffffff;
  --star:#f2c230;
}
*{box-sizing:border-box;margin:0;padding:0}
html,body{width:1200px;height:4898px;overflow:hidden;background:var(--bg);color:var(--text);font-family:"Saira",sans-serif}
.page{position:relative;width:1200px;height:4898px}
section,header,footer{position:absolute;left:0;width:1200px;overflow:hidden}
.wrap{position:relative;width:890px;margin:0 auto;height:100%}
h1,h2,h3{font-weight:400;color:var(--text)}
p{color:var(--muted)}
.btn{display:inline-block;height:30px;line-height:28px;padding:0 18px;border-radius:3px;font-size:11px;border:1px solid var(--white);white-space:nowrap}
.btn-solid{background:var(--white);color:#111}
.btn-ghost{color:var(--text);border-color:#9a9a9a}
.btns{display:flex;gap:12px}
.img{position:absolute;border-radius:40px}
.eyebrow{font-size:11px;color:var(--text);font-weight:500;margin-bottom:4px}

/* header + hero */
.hero{top:0;height:560px;background:radial-gradient(ellipse at 68% 45%,#4a4540 0%,#24211e 35%,#0e0d0c 75%)}
.hero-photo{position:absolute;inset:0;background:linear-gradient(180deg,rgba(0,0,0,.35),rgba(0,0,0,0) 30%,rgba(0,0,0,.7) 100%),radial-gradient(ellipse 420px 150px at 720px 300px,#3d4248 0%,rgba(40,40,40,0) 100%)}
.nav{position:absolute;top:14px;left:155px;right:155px;display:flex;align-items:center;height:30px}
.brand{display:flex;align-items:center;gap:8px;font-size:22px;font-weight:300;color:var(--text)}
.brand i{width:12px;height:12px;background:var(--white);display:block}
.nav-links{margin-left:auto;display:flex;gap:22px;font-size:10px;color:var(--text);align-items:center}
.nav-links .btn{height:24px;line-height:22px;padding:0 16px;font-size:10px}
.hero-copy{position:absolute;left:230px;top:215px;width:260px}
.hero-copy h1{font-size:26px;line-height:1.25;font-weight:500}
.hero-copy p{font-size:10px;line-height:1.5;margin:18px 0 22px}

/* divider band */
.divider{position:absolute;left:0;width:1200px;height:100px;background:radial-gradient(ellipse 340px 24px at 50% 50%,rgba(255,255,255,.35) 0%,rgba(255,255,255,.08) 55%,rgba(0,0,0,0) 100%),var(--bg)}

/* ownership */
.ownership{top:640px;height:460px;background:var(--bg)}
.ownership .copy{position:absolute;left:0;top:50px;width:370px}
.ownership h2{font-size:24px;line-height:1.3}
.ownership .copy>p{font-size:10px;line-height:1.6;margin:20px 0}
.feats{display:flex;gap:26px;margin-bottom:30px}
.feat{width:90px;font-size:9px;color:var(--text);line-height:1.3}
.ico{width:40px;height:40px;border-radius:50%;background:var(--white);display:flex;align-items:center;justify-content:center;margin-bottom:10px}
.ownership .img{right:0;top:30px;width:432px;height:334px;background:linear-gradient(135deg,#545454,#2a2a2a 55%,#6b6b6b)}

/* options */
.options{top:1100px;height:460px;background:linear-gradient(180deg,#161616,#0d0d0d)}
.options .img{left:0;top:80px;width:432px;height:305px;background:linear-gradient(180deg,#6a9ccd 0%,#e0b27a 55%,#6b4c32 100%)}
.opt-list{position:absolute;left:495px;top:125px;width:360px;border-left:1px solid var(--line);padding-left:18px}
.opt{margin-bottom:22px}
.opt h3{font-size:13px;margin-bottom:4px}
.opt p{font-size:9.5px;line-height:1.45}

/* unparalleled */
.unpar{top:1560px;height:500px;background:var(--bg)}
.unpar .copy{position:absolute;left:0;top:110px;width:380px}
.unpar h2{font-size:24px;line-height:1.3}
.unpar .copy>p{font-size:10px;line-height:1.6;margin:16px 0 22px}
.pair{display:flex;gap:20px;margin-bottom:34px}
.pair div.item{display:flex;gap:10px;width:180px}
.pair .ico{flex:none;width:36px;height:36px}
.pair h3{font-size:11px;margin-bottom:4px}
.pair p{font-size:9px;line-height:1.4}
.unpar .img{right:0;top:100px;width:432px;height:334px;background:linear-gradient(135deg,#3c4347,#1d2022 50%,#6a5a4a)}

/* services */
.services{top:2060px;height:360px;text-align:center}
.services .eyebrow{margin-top:100px}
.services h2{font-size:26px}
.services .lead{font-size:10px;line-height:1.6;width:620px;margin:14px auto 26px}
.svc-row{display:flex;justify-content:center;gap:80px}
.svc{width:170px;display:flex;flex-direction:column;align-items:center}
.svc .ico{width:52px;height:52px}
.svc h3{font-size:11px;font-weight:500;line-height:1.3}
.svc p{font-size:9px;line-height:1.4;margin-top:6px}
.services .btns{justify-content:center;margin-top:24px}

/* cta box */
.ctabox{top:2420px;height:260px}
.ctabox .box{position:absolute;left:237px;top:40px;width:656px;height:190px;background:var(--panel);border-radius:24px;text-align:center;padding-top:40px}
.ctabox h2{font-size:24px}
.ctabox p{font-size:10px;color:var(--text);margin:6px 0 22px}
.ctabox .btns{justify-content:center}

/* testimonial */
.testimonial{top:2680px;height:310px;text-align:center}
.quote{width:54px;height:54px;border-radius:50%;border:2px solid var(--white);margin:40px auto 10px;font-size:34px;line-height:56px;font-weight:600}
.stars{color:var(--star);font-size:18px;letter-spacing:4px}
.testimonial .txt{font-size:11px;line-height:1.8;color:var(--text);width:720px;margin:12px auto 20px}
.arrow{position:absolute;top:135px;font-size:20px;color:var(--muted)}
.person{display:flex;justify-content:center;align-items:center;gap:12px}
.avatar{width:36px;height:36px;border-radius:50%;background:#6d6d6d}
.who{text-align:left;font-size:10px;line-height:1.3}
.who span{display:block;color:var(--muted);font-size:9px}
.chip{width:92px;height:34px;background:var(--white);border-radius:5px;display:flex;align-items:center;justify-content:center}
.chip i{width:14px;height:14px;border-radius:50%;background:#c9303b;display:block}

/* trusted */
.trusted{top:2990px;height:310px;background:linear-gradient(180deg,#050505,#121212);text-align:center}
.trusted h3{font-size:13px;margin-top:60px}
.logos{display:flex;justify-content:center;gap:14px;margin-top:24px}
.logo-card{width:126px;height:64px;background:var(--white);border-radius:10px;display:flex;align-items:center;justify-content:center}
.logo-card i{width:20px;height:20px;border-radius:50%;display:block}
.trusted .btn{margin-top:32px;height:26px;line-height:24px;font-size:10px}

/* newsletter */
.newsletter{top:3300px;height:260px;background:#090909}
.nl-box{position:absolute;left:237px;top:20px;width:656px;height:220px;border:1px solid var(--line);border-radius:18px;background:linear-gradient(90deg,#141414,#1d1d1d);padding:36px 42px}
.nl-box h2{font-size:25px;line-height:1.2}
.nl-box .sub{font-size:9.5px;margin:8px 0 14px}
.field{width:312px;height:32px;background:var(--white);border-radius:4px;display:flex;align-items:center;justify-content:space-between;padding:0 12px;font-size:9px;color:#888}
.nl-box .fine{font-size:8px;color:var(--dim);margin-top:8px}
.nl-art{position:absolute;right:40px;top:30px;width:190px;height:140px;border-radius:16px;background:radial-gradient(ellipse at 50% 50%,#555 0%,rgba(30,30,30,0) 70%)}

/* faq */
.faq{top:3560px;height:580px;background:var(--bg)}
.faq .img{left:0;top:70px;width:336px;height:430px;background:linear-gradient(160deg,#d9d3c6 0%,#6e6a64 45%,#1a1a1a 100%)}
.faq-side{position:absolute;left:375px;top:70px;width:515px}
.faq-side h2{font-size:24px}
.faq-side .lead{font-size:10px;margin:6px 0 26px}
.q{border-bottom:1px solid var(--line);padding:14px 10px;display:flex;justify-content:space-between;font-size:10px;color:var(--text)}
.q-open{display:block}
.q-open .row{display:flex;justify-content:space-between}
.q-open p{font-size:9px;line-height:1.5;margin-top:16px;width:400px}
.still{display:flex;justify-content:space-between;align-items:center;margin-top:30px}
.still h3{font-size:13px}
.still p{font-size:9px}
.still .btn{height:24px;line-height:22px;font-size:9px}

/* cta2 */
.cta2{top:4140px;height:280px;text-align:center}
.cta2 h2{font-size:25px;margin-top:40px}
.cta2 p{font-size:10px;line-height:1.6;width:620px;margin:32px auto 26px}
.cta2 .btns{justify-content:center}

/* footer */
.footer{top:4520px;height:378px;background:linear-gradient(180deg,#151515,#0a0a0a)}
.foot-top{position:absolute;top:30px;left:0;right:0;display:flex}
.foot-top .brand{width:225px;align-self:flex-start}
.col{width:130px;font-size:10px}
.col h4{font-weight:500;margin-bottom:8px;font-size:11px}
.col a{display:block;color:var(--muted);line-height:1.6;text-decoration:none}
.subscribe{margin-left:auto;width:280px;font-size:10px}
.subscribe h4{font-weight:500;font-size:11px;margin-bottom:6px}
.subscribe p{font-size:9px}
.subscribe .field{width:280px;height:30px;margin:14px 0 6px}
.foot-bottom{position:absolute;top:290px;left:0;right:0;display:flex;align-items:center;font-size:9px;color:var(--muted);gap:16px}
.foot-bottom .social{margin-left:auto;display:flex;gap:8px}
.social i{width:9px;height:9px;border-radius:50%;background:var(--muted);display:block}
</style>
</head>
<body>
<div class="page">

<header class="hero">
  <div class="hero-photo" role="img" aria-label="Large-cabin private jet parked in a dimly lit hangar at night with crew nearby"></div>
  <nav class="nav">
    <div class="brand">Quorvel<i></i></div>
    <div class="nav-links">
      <span>Aircraft</span><span>Programs</span><span>Why Quorvel</span><span>Lifestyle ⌄</span>
      <span class="btn btn-ghost">Inquiry</span><span class="btn btn-solid">Sign Up</span>
    </div>
  </nav>
  <div class="hero-copy">
    <h1>Experience the<br>Ultimate in Luxury<br>Jet Travel</h1>
    <p>Quorvel offers fractional jet ownership, jet card programs, private jet lease programs, all access programs, and by the seat charter flights. Discover the perfect flight program for your needs.</p>
    <div class="btns"><span class="btn btn-solid">Explore</span><span class="btn btn-ghost">Learn More</span></div>
  </div>
</header>

<div class="divider" style="top:540px" role="img" aria-label="Decorative wing-and-emblem divider"></div>

<section class="ownership">
  <div class="wrap">
    <div class="copy">
      <h2>Experience the Luxury of<br>Fractional Jet Ownership</h2>
      <p>With Quorvel's fractional jet ownership program, you can enjoy the benefits of private jet travel without the hassle and expense of owning a whole aircraft. Our program offers flexibility, convenience, and access to a fleet of luxurious jets, allowing you to travel in style and comfort.</p>
      <div class="feats">
        <div class="feat"><div class="ico"><svg width="18" height="18" viewBox="0 0 24 24"><path d="M2 14l20-6-6 10-3-4-11 0z" fill="#111"/></svg></div>Flexible Ownership Options</div>
        <div class="feat"><div class="ico"><svg width="18" height="18" viewBox="0 0 24 24"><rect x="4" y="5" width="16" height="15" rx="2" fill="#111"/></svg></div>Convenient Booking Process</div>
        <div class="feat"><div class="ico"><svg width="18" height="18" viewBox="0 0 24 24"><path d="M11 4h2v16h-2zM4 11h16v2H4z" fill="#111"/></svg></div>Luxurious Fleet of Jets</div>
      </div>
      <div class="btns"><span class="btn btn-solid">Learn More</span><span class="btn btn-ghost">Sign Up</span></div>
    </div>
    <div class="img" role="img" aria-label="Confident traveller in a grey suit seated in a jet cabin"></div>
  </div>
</section>

<section class="options">
  <div class="wrap">
    <div class="img" role="img" aria-label="Businessman in a leather armchair floating above a city skyline with jets in the sky"></div>
    <div class="opt-list">
      <div class="opt"><h3>Flexible Ownership Options Available</h3><p>Choose from a variety of ownership programs and enjoy the freedom to fly on your own terms.</p></div>
      <div class="opt"><h3>Convenient Jet Card Programs</h3><p>Access a fleet of private jets with our exclusive jet card programs, offering flexibility and convenience.</p></div>
      <div class="opt"><h3>Flexible Lease Programs</h3><p>Experience the luxury of private jet travel without the commitment with our flexible lease programs.</p></div>
    </div>
  </div>
</section>

<section class="unpar">
  <div class="wrap">
    <div class="copy">
      <div class="eyebrow">Experience</div>
      <h2>Unparalleled Luxury and<br>Convenience for Private Aviation</h2>
      <p>Discover the ultimate in luxury and convenience with Quorvel. Our exclusive private aviation solutions provide you with unparalleled access to the world of private jets, ensuring a seamless and extraordinary travel experience.</p>
      <div class="pair">
        <div class="item"><div class="ico"><svg width="16" height="16" viewBox="0 0 24 24"><circle cx="12" cy="12" r="8" fill="#111"/></svg></div><div><h3>Convenience</h3><p>Enjoy hassle-free travel with our flexible scheduling and personalized services.</p></div></div>
        <div class="item"><div class="ico"><svg width="16" height="16" viewBox="0 0 24 24"><path d="M4 11h12l-4-4 1.5-1.5L20 12l-6.5 6.5L12 17l4-4H4z" fill="#111"/></svg></div><div><h3>Luxury</h3><p>Indulge in the lavish amenities and exquisite interiors of our private jets.</p></div></div>
      </div>
      <div class="btns"><span class="btn btn-solid">Learn More</span><span class="btn btn-ghost">Sign Up</span></div>
    </div>
    <div class="img" role="img" aria-label="Smiling pilot with headset in a cockpit"></div>
  </div>
</section>

<section class="services">
  <div class="eyebrow">Luxury</div>
  <h2>Experience the Ultimate in Private Jet Travel</h2>
  <p class="lead">Quorvel offers a wide range of exclusive services to meet your private jet travel needs. From fractional jet ownership to on-demand charter flights, we provide the highest level of luxury and convenience.</p>
  <div class="svc-row">
    <div class="svc"><div class="ico"><svg width="22" height="22" viewBox="0 0 24 24"><path d="M2 14l20-6-6 10-3-4z" fill="#111"/></svg></div><h3>On-Demand Charter</h3><p>Fly anywhere, anytime with our on-demand charter service.</p></div>
    <div class="svc"><div class="ico"><svg width="22" height="22" viewBox="0 0 24 24"><circle cx="12" cy="12" r="9" fill="none" stroke="#111" stroke-width="2"/><path d="M3 12h18M12 3v18" stroke="#111" stroke-width="2"/></svg></div><h3>Global Medical Response &amp;<br>Recovery</h3><p>We provide specialized medical transportation services worldwide.</p></div>
    <div class="svc"><div class="ico"><svg width="22" height="22" viewBox="0 0 24 24"><path d="M3 11h18v2H3zM11 4h2v16h-2z" fill="#111"/></svg></div><h3>Fractional Jet Ownership</h3><p>Enjoy the benefits of owning a private jet without the hassles.</p></div>
  </div>
  <div class="btns"><span class="btn btn-solid">Learn More</span><span class="btn btn-ghost">Sign Up</span></div>
</section>

<section class="ctabox">
  <div class="box">
    <h2>Experience luxury travel like never before</h2>
    <p>Contact us today to book your exclusive jet experience</p>
    <div class="btns"><span class="btn btn-solid">Learn More</span><span class="btn btn-ghost">Sign Up</span></div>
  </div>
</section>

<section class="testimonial">
  <div class="quote">“</div>
  <div class="stars">★★★★★</div>
  <p class="txt">Lorem Ipsum Is Simply Dummy Text Of The Printing And Typesetting Industry. Lorem Ipsum Has Been The Industry's Standard Dummy Text Ever Since The 1500s, When An Unknown Printer Took A Galley Of Type And Scrambled It To Make A Type Specimen Book. It Has Survived Not Only Five Centuries, But Also The Leap Into Electronic Typesetting, Remaining Essentially Unchanged.</p>
  <span class="arrow" style="left:243px">‹</span><span class="arrow" style="right:243px">›</span>
  <div class="person">
    <div class="avatar" role="img" aria-label="Client portrait"></div>
    <div class="who">Elan Varro<span>CEO, Norrell Group</span></div>
    <div class="chip"><i></i></div>
  </div>
</section>

<section class="trusted">
  <h3>Trusted By Top-Tier Companies Around The Globe</h3>
  <div class="logos">
    <div class="logo-card"><i style="background:#47c16a"></i></div>
    <div class="logo-card"><i style="background:#f08a24"></i></div>
    <div class="logo-card"><i style="background:#2a7fd4"></i></div>
    <div class="logo-card"><i style="background:#d8323b"></i></div>
    <div class="logo-card"><i style="background:#e9a12a"></i></div>
  </div>
  <span class="btn btn-ghost">View All</span>
</section>

<section class="newsletter">
  <div class="nl-box">
    <h2>Subscribe to our<br>Newsletter</h2>
    <p class="sub">Stay updated with exclusive offers and industry news</p>
    <div class="field"><span>Your email address</span><svg width="12" height="12" viewBox="0 0 24 24"><path d="M2 12l20-9-7 19-3-8z" fill="#111"/></svg></div>
    <p class="fine">By joining, you agree to our Terms and Conditions</p>
    <div class="nl-art" role="img" aria-label="Paper plane in glowing dark space"></div>
  </div>
</section>

<section class="faq">
  <div class="wrap">
    <div class="img" role="img" aria-label="Traveller gazing out a jet window at mountains beside a large question mark"></div>
    <div class="faq-side">
      <h2>Frequently</h2>
      <p class="lead">Find answers to common questions about Quorvel's services and programs.</p>
      <div class="q"><span>What is Quorvel?</span><span>+</span></div>
      <div class="q q-open"><div class="row"><span>How it works?</span><span>−</span></div>
        <p>Quorvel is a company that offers fractional jet ownership, jet card programs, private jet lease programs, all access programs, helicopter access programs, and by the seat charter flights. We provide flexible and convenient options for individuals and businesses to access private aviation services.</p></div>
      <div class="q"><span>Why choose Quorvel?</span><span>+</span></div>
      <div class="q"><span>How to book?</span><span>+</span></div>
      <div class="q"><span>What are the benefits?</span><span>+</span></div>
      <div class="still"><div><h3>Still have questions?</h3><p>Contact us for more information</p></div><span class="btn btn-ghost">Contact</span></div>
    </div>
  </div>
</section>

<section class="cta2">
  <h2>Experience luxury travel like never before</h2>
  <p>Discover the ultimate in private jet travel with Quorvel. Whether you're looking for fractional jet ownership, jet card programs, private jet lease programs, all access programs, helicopter access programs, or by the seat charter flights, we have the perfect solution for your travel needs.</p>
  <div class="btns"><span class="btn btn-solid">Book</span><span class="btn btn-ghost">Contact</span></div>
</section>

<div class="divider" style="top:4420px" role="img" aria-label="Decorative wing-and-emblem divider"></div>

<footer class="footer">
  <div class="wrap">
    <div class="foot-top">
      <div class="brand">Quorvel<i></i></div>
      <div class="col"><h4>About Us</h4><a>Charter</a><a>Fleet</a><a>Destinations</a><a>Pricing</a><a>Contact</a></div>
      <div class="col"><h4>Services</h4><a>Private Jets</a><a>Helicopters</a><a>Jet Cards</a><a>Membership</a><a>FAQ</a></div>
      <div class="col"><h4>Terms</h4><a>Privacy</a><a>Careers</a><a>Press</a><a>Blog</a><a>Support</a></div>
      <div class="subscribe"><h4>Subscribe to our Newsletter</h4><p>Join our mailing list for the latest updates.</p>
        <div class="field"><span>Enter email address</span><svg width="12" height="12" viewBox="0 0 24 24"><path d="M2 12l20-9-7 19-3-8z" fill="#111"/></svg></div>
        <p>By subscribing, you agree to our Privacy Policy and consent to receive updates.</p></div>
    </div>
    <div class="foot-bottom">
      <span>© 2024 Quorvel. All rights reserved.</span><span>Privacy Policy</span><span>Terms of Service</span><span>Cookie Settings</span>
      <div class="social"><i></i><i></i><i></i><i></i><i></i></div>
    </div>
  </div>
</footer>

</div>
</body>
</html>
```